BRAVO Estate Steward

We require a website built for this company. Logo is also on the attached document. Some info on the company:<br/>To create a work class experience for our clients for property maintenance. A personalised service that deliver’s what landlords need...Quality work, on time and managed from start to finish.<br/>We do things different, our clients deal with one contact, a client manager who manages your maintenance task from start to finish. Our service allows our expert trades people to do what they do best and leave the management/organising to us!<br/>I have drafted up the layout of the web ... very brief at this stage however once we have more info we will add links and can collate more information and provide. <br/>We just want to get a layout of what you think the web should look like and can go from there.

```html
<!DOCTYPE html>
<html lang="en">
<head>
<meta charset="utf-8">
<title>BRAVO Estate Steward</title>
<link href="https://fonts.googleapis.com/css2?family=Lato:wght@400;700;900&display=swap" rel="stylesheet">
<style>
:root{
  --gold:#f6b512;
  --gold-deep:#e9a800;
  --ink:#2f2f2f;
  --dark:#333333;
  --text:#555555;
  --muted:#777777;
  --paper:#ffffff;
  --mist:#eeeeee;
  --line:#dddddd;
}
*{margin:0;padding:0;box-sizing:border-box}
html,body{width:1200px;height:4831px;overflow:hidden}
body{font-family:'Lato',sans-serif;color:var(--text);background:var(--paper);position:relative}
.abs{position:absolute}
.center{text-align:center}
.btn{position:absolute;background:var(--gold);color:#fff;font-weight:700;font-size:16px;display:flex;align-items:center;justify-content:center;border-radius:3px;text-transform:uppercase;box-shadow:0 3px 0 var(--gold-deep)}
.section-title{position:absolute;left:0;width:1200px;text-align:center;color:var(--ink);font-weight:700;font-size:38px}
.rule{position:absolute;left:568px;width:64px;height:4px;background:var(--gold)}

/* hero */
.hero{position:absolute;left:0;top:0;width:1200px;height:731px;background:linear-gradient(180deg,#5f7890 0%,#6f8196 35%,#55603f 62%,#3d5a24 100%)}
.hero-shade{position:absolute;left:0;top:0;width:1200px;height:731px;background:rgba(20,30,50,.35)}
.brand{position:absolute;left:141px;top:58px;display:flex;align-items:center;gap:12px;color:#fff;font-size:30px;font-weight:700;line-height:1}
.brand-mark{width:26px;height:26px;background:var(--gold)}
.call{position:absolute;left:677px;top:34px;display:flex;align-items:center;gap:12px;color:#fff}
.call-icon{width:38px;height:38px;border-radius:50%;background:var(--gold);display:flex;align-items:center;justify-content:center}
.call small{display:block;font-size:14px}
.call strong{font-size:24px;font-weight:700}
.nav{position:absolute;left:456px;top:104px;display:flex;gap:31px;font-size:15px;color:#fff}
.nav .on{color:var(--gold)}
.hero-title{position:absolute;left:0;top:345px;width:1200px;text-align:center;color:#fff;font-size:58px;font-weight:700}
.play{position:absolute;left:570px;top:271px}
.arrow-round{position:absolute;width:30px;height:30px;border-radius:50%;background:#222;display:flex;align-items:center;justify-content:center}

/* services */
.card{position:absolute;background:#fff;box-shadow:0 2px 12px rgba(0,0,0,.18);text-align:center}
.svc-icon{display:block;margin:22px auto 0}
.svc-title{font-size:19px;color:var(--ink);margin-top:10px}
.svc-text{font-size:13px;line-height:24px;color:var(--text);margin:12px 24px 0}

/* welcome */
.welcome-photo{position:absolute;left:0;top:1646px;width:640px;height:495px;background:linear-gradient(180deg,#7ea3c7 0%,#a6865f 40%,#6d8a45 75%,#c8a08d 100%)}
.welcome-panel{position:absolute;left:0;top:1646px}
.welcome-title{position:absolute;left:669px;top:1708px;width:460px;font-size:39px;line-height:49px;color:#fff;font-weight:400}
.welcome-text{position:absolute;left:669px;top:1860px;width:440px;font-size:15.5px;line-height:29px;color:#e8e8e8}

/* benefit */
.benefit{position:absolute;left:0;top:2141px;width:1200px;height:475px;background:var(--gold)}
.benefit-item{position:absolute;top:2331px;width:191px;text-align:center}
.benefit-item + .benefit-item{border-left:1px solid rgba(255,255,255,.35)}
.benefit-icon{width:90px;height:90px;border-radius:50%;background:var(--dark);margin:0 auto;border:3px solid rgba(0,0,0,.15);display:flex;align-items:center;justify-content:center}
.benefit-name{font-size:16px;font-weight:700;color:var(--ink);margin-top:23px}
.benefit-text{font-size:14px;line-height:20px;color:#3d3d3d;margin-top:12px}

/* appointment */
.skyline{position:absolute;left:60px;top:2840px;width:1080px;height:231px;background:linear-gradient(180deg,rgba(220,220,220,0) 0%,rgba(220,220,220,.45) 100%)}
.appt-title{position:absolute;left:0;width:1200px;text-align:center;color:var(--ink);font-weight:700;font-size:39px}
.appt-text{position:absolute;left:200px;top:2800px;width:800px;text-align:center;font-size:15px;line-height:29px;color:var(--text)}

/* news */
.news{position:absolute;left:0;top:3071px;width:1200px;height:660px;background:var(--mist)}
.news-photo{position:absolute;left:6px;top:6px;width:274px;height:179px}
.date{position:absolute;left:117px;top:164px;width:52px;height:52px;border-radius:50%;background:var(--gold);border:3px solid #fff;font-size:10px;font-weight:700;color:var(--ink);display:flex;flex-direction:column;align-items:center;justify-content:center;line-height:12px}
.news-title{position:absolute;left:16px;top:228px;width:254px;font-size:16.5px;line-height:26px;color:var(--ink);font-weight:400}
.news-text{position:absolute;left:26px;top:286px;width:234px;font-size:13.5px;line-height:24px;color:var(--text)}

/* testimonials */
.quote-text{position:absolute;left:26px;top:28px;width:355px;font-size:13px;line-height:24px;color:var(--text)}
.avatar{position:absolute;left:30px;top:160px;width:70px;height:70px;border-radius:50%;background:linear-gradient(160deg,#d8c8bb,#8a7668)}
.quote-mark{position:absolute;left:124px;top:150px;font-size:40px;color:#999;font-weight:900;line-height:1}
.who{position:absolute;left:124px;top:184px;font-size:14px;line-height:24px;color:var(--ink)}
.who b{font-weight:400;text-transform:uppercase}

/* contact */
.footer{position:absolute;left:0;top:4256px;width:1200px;height:575px;background:var(--dark)}
.field{position:absolute;border:1px solid #bdbdbd;color:#ddd;font-size:11px;padding:0 16px;display:flex;align-items:center}
.field.area{align-items:flex-start;padding-top:10px}
.info-icon{position:absolute;left:736px;width:46px;height:46px;border-radius:50%;border:2px solid #999;display:flex;align-items:center;justify-content:center}
.info-text{position:absolute;left:803px;width:300px;font-size:13.5px;line-height:24px;color:#eee}
.copyright{position:absolute;left:152px;top:4765px;font-size:13px;color:#eee}
.social{position:absolute;top:4760px;width:32px;height:32px;border-radius:50%;border:1.5px solid #ccc}
</style>
</head>
<body>

<!-- hero -->
<section class="hero" role="img" aria-label="Photo of a large suburban house with a green lawn under a cloudy sky"></section>
<div class="hero-shade"></div>

<div class="brand"><span class="brand-mark"></span><span>BRAVO Estate Steward</span></div>

<div class="call">
  <div class="call-icon">
    <svg width="20" height="20" viewBox="0 0 24 24"><path fill="#fff" d="M6.6 10.8a15 15 0 0 0 6.6 6.6l2.2-2.2c.3-.3.7-.4 1-.2 1.1.4 2.3.6 3.6.6.6 0 1 .4 1 1V20c0 .6-.4 1-1 1A17 17 0 0 1 3 4c0-.6.4-1 1-1h3.5c.6 0 1 .4 1 1 0 1.3.2 2.5.6 3.6.1.3 0 .7-.2 1z"/></svg>
  </div>
  <div><small>Call Now</small><strong>555 0142 7788</strong></div>
</div>
<div class="btn" style="left:915px;top:38px;width:139px;height:37px;font-size:13px">Get Started</div>

<nav class="nav">
  <span class="on">HOME</span><span>ABOUT US</span><span>OUR SERVICES</span><span>BENEFIT</span><span>BLOG</span><span>CONTACT US</span>
</nav>

<svg class="play" width="60" height="60" viewBox="0 0 60 60"><circle cx="30" cy="30" r="27" fill="none" stroke="#fff" stroke-width="2.5"/><path d="M24 18 L42 30 L24 42 Z" fill="none" stroke="#fff" stroke-width="2.5" stroke-linejoin="round"/></svg>
<h1 class="hero-title">BRAVO Estate Steward</h1>
<div class="btn" style="left:503px;top:450px;width:195px;height:41px">Get More Info</div>

<div class="arrow-round" style="left:71px;top:351px"><svg width="12" height="12" viewBox="0 0 12 12"><path d="M8 1 L3 6 L8 11" stroke="#fff" stroke-width="2" fill="none"/></svg></div>
<div class="arrow-round" style="left:1097px;top:351px"><svg width="12" height="12" viewBox="0 0 12 12"><path d="M4 1 L9 6 L4 11" stroke="#fff" stroke-width="2" fill="none"/></svg></div>

<svg class="abs" style="left:0;top:640px" width="1200" height="95" viewBox="0 0 1200 95">
  <path d="M0 25 Q600 95 1200 25 L1200 95 L0 95 Z" fill="var(--gold)"/>
  <path d="M0 42 Q600 96 1200 52 L1200 95 L0 95 Z" fill="#fff"/>
</svg>

<!-- services -->
<h2 class="section-title" style="top:795px">Our Services</h2>
<div class="rule" style="top:857px"></div>

<div class="card" style="left:137px;top:915px;width:291px;height:285px">
  <svg class="svc-icon" width="68" height="68" viewBox="0 0 68 68" fill="none" stroke="var(--gold)" stroke-width="2.5" stroke-linecap="round" stroke-linejoin="round"><path d="M14 54 L38 30"/><path d="M36 18 a12 12 0 0 0 14 14 l-6 -6 4 -4 6 6 a12 12 0 0 0 -14 -14 z"/><path d="M10 58 l6 -6"/><rect x="8" y="52" width="8" height="8" rx="1"/></svg>
  <div class="svc-title">Trade people</div>
  <p class="svc-text">Sed ut perspiciatis unde omnis iste natus error sit voluptatem accusantium doloque laudantium, totam rem aperiam, eaque ipsa quae ab illo inventore veritatis et quasi architecto beatae vitae</p>
</div>
<div class="card" style="left:454px;top:915px;width:291px;height:285px">
  <svg class="svc-icon" width="68" height="68" viewBox="0 0 68 68" fill="none" stroke="var(--gold)" stroke-width="2.5" stroke-linecap="round" stroke-linejoin="round"><rect x="6" y="20" width="36" height="26" rx="2"/><path d="M42 28 h10 l8 9 v9 h-18 z"/><circle cx="18" cy="48" r="5" fill="#fff"/><circle cx="50" cy="48" r="5" fill="#fff"/></svg>
  <div class="svc-title">Removalist van and trailers</div>
  <p class="svc-text">Sed ut perspiciatis unde omnis iste natus error sit voluptatem accusantium doloque laudantium, totam rem aperiam, eaque ipsa quae ab illo inventore veritatis et quasi architecto beatae vitae</p>
</div>
<div class="card" style="left:773px;top:915px;width:291px;height:285px">
  <svg class="svc-icon" width="68" height="68" viewBox="0 0 68 68" fill="none" stroke="var(--gold)" stroke-width="2.5" stroke-linecap="round"><circle cx="34" cy="34" r="7"/><circle cx="14" cy="14" r="7"/><circle cx="54" cy="14" r="7"/><circle cx="14" cy="54" r="7"/><circle cx="54" cy="54" r="7"/><path d="M19 19 L29 29 M49 19 L39 29 M19 49 L29 39 M49 49 L39 39"/></svg>
  <div class="svc-title">Connections</div>
  <p class="svc-text">Sed ut perspiciatis unde omnis iste natus error sit voluptatem accusantium doloque laudantium, totam rem aperiam, eaque ipsa quae ab illo inventore veritatis et quasi architecto beatae vitae</p>
</div>
<div class="card" style="left:137px;top:1234px;width:291px;height:289px">
  <svg class="svc-icon" width="68" height="68" viewBox="0 0 68 68" fill="none" stroke="var(--gold)" stroke-width="2.5" stroke-linecap="round"><circle cx="34" cy="34" r="27"/><circle cx="34" cy="34" r="17"/><circle cx="34" cy="34" r="6"/><path d="M34 10 v3 M34 55 v3"/></svg>
  <div class="svc-title">Smoke alarms</div>
  <p class="svc-text">Sed ut perspiciatis unde omnis iste natus error sit voluptatem accusantium doloque laudantium, totam rem aperiam, eaque ipsa quae ab illo inventore veritatis et quasi architecto beatae vitae</p>
</div>
<div class="card" style="left:454px;top:1234px;width:291px;height:289px">
  <svg class="svc-icon" width="68" height="68" viewBox="0 0 68 68" fill="none" stroke="var(--gold)" stroke-width="2.5" stroke-linecap="round" stroke-linejoin="round"><circle cx="36" cy="20" r="13"/><path d="M40 14 h-6 a3 3 0 0 0 0 6 h4 a3 3 0 0 1 0 6 h-6 M36 11 v3 M36 26 v3"/><path d="M6 50 h10 l12 -6 h14 a3 3 0 0 1 0 6 h-10 M16 58 h22 l20 -12 a3 3 0 0 0 -4 -5 l-12 7"/></svg>
  <div class="svc-title">Finance</div>
  <p class="svc-text">Sed ut perspiciatis unde omnis iste natus error sit voluptatem accusantium doloque laudantium, totam rem aperiam, eaque ipsa quae ab illo inventore veritatis et quasi architecto beatae vitae</p>
</div>
<div class="card" style="left:773px;top:1234px;width:291px;height:289px">
  <svg class="svc-icon" width="68" height="68" viewBox="0 0 68 68" fill="none" stroke="var(--gold)" stroke-width="2.5" stroke-linecap="round" stroke-linejoin="round"><path d="M8 60 h52"/><rect x="12" y="42" width="9" height="18"/><rect x="29" y="32" width="9" height="28"/><rect x="46" y="22" width="9" height="38"/><path d="M10 30 L26 18 L36 24 L56 8 M48 8 h8 v8"/></svg>
  <div class="svc-title">Wealth creation</div>
  <p class="svc-text">Sed ut perspiciatis unde omnis iste natus error sit voluptatem accusantium doloque laudantium, totam rem aperiam, eaque ipsa quae ab illo inventore veritatis et quasi architecto beatae vitae</p>
</div>

<!-- welcome -->
<div class="welcome-photo" role="img" aria-label="Photo of brick apartment buildings with balconies beside a flowering garden path"></div>
<svg class="welcome-panel" width="1200" height="495" viewBox="0 0 1200 495"><path d="M634 0 L1200 0 L1200 495 L572 495 Z" fill="var(--dark)"/></svg>
<h2 class="welcome-title">Welcome to BRAVO Estate Steward</h2>
<div class="abs" style="left:669px;top:1832px;width:76px;height:4px;background:#fff"></div>
<p class="welcome-text">Sed ut perspiciatis unde omnis iste natus error sit vm doloremque laudantium, totam rem aperiam, eaque ipsa quae ab illo inventore veritatis et quasi archicto beatae vitae dicta sunt explicabo. Nemo enim ipsam voluptatem quia voluptas sit aspernatur</p>
<div class="btn" style="left:669px;top:2033px;width:137px;height:35px;font-size:14px;color:var(--ink)">Read More</div>

<!-- benefit -->
<section class="benefit"></section>
<h2 class="section-title" style="top:2203px">Bravo Benefit</h2>
<div class="rule" style="top:2268px;background:var(--ink);left:563px;width:74px"></div>

<div class="benefit-item" style="left:120px"><div class="benefit-icon"><svg width="44" height="44" viewBox="0 0 44 44" fill="none" stroke="var(--gold)" stroke-width="2" stroke-linecap="round"><path d="M8 24 v-4 a14 14 0 0 1 28 0 v4"/><rect x="5" y="23" width="6" height="10" rx="2"/><rect x="33" y="23" width="6" height="10" rx="2"/><path d="M36 33 q0 6 -10 6 h-4"/></svg></div><div class="benefit-name">Customer service</div><p class="benefit-text">Nemo enim ipsam vuptatem quia voluptas sit aspernatur aut</p></div>
<div class="benefit-item" style="left:311px"><div class="benefit-icon"><svg width="40" height="40" viewBox="0 0 24 24"><path fill="none" stroke="var(--gold)" stroke-width="1.4" d="M6.6 10.8a15 15 0 0 0 6.6 6.6l2.2-2.2c.3-.3.7-.4 1-.2 1.1.4 2.3.6 3.6.6.6 0 1 .4 1 1V20c0 .6-.4 1-1 1A17 17 0 0 1 3 4c0-.6.4-1 1-1h3.5c.6 0 1 .4 1 1 0 1.3.2 2.5.6 3.6.1.3 0 .7-.2 1z"/></svg></div><div class="benefit-name">Call centre</div><p class="benefit-text">Nemo enim ipsam vuptatem quia voluptas sit aspernatur aut</p></div>
<div class="benefit-item" style="left:503px"><div class="benefit-icon"><svg width="44" height="44" viewBox="0 0 44 44" fill="none" stroke="var(--gold)" stroke-width="2" stroke-linecap="round" stroke-linejoin="round"><circle cx="22" cy="22" r="16"/><path d="M14 22 l6 6 l10 -12"/></svg></div><div class="benefit-name">Values</div><p class="benefit-text">Nemo enim ipsam vuptatem quia voluptas sit aspernatur aut</p></div>
<div class="benefit-item" style="left:694px"><div class="benefit-icon"><svg width="44" height="44" viewBox="0 0 44 44" fill="none" stroke="var(--gold)" stroke-width="2" stroke-linejoin="round"><path d="M6 22 L22 6 h16 v16 L22 38 z"/><circle cx="31" cy="13" r="3"/></svg></div><div class="benefit-name">Pricing</div><p class="benefit-text">Nemo enim ipsam vuptatem quia voluptas sit aspernatur aut</p></div>
<div class="benefit-item" style="left:885px"><div class="benefit-icon"><svg width="44" height="44" viewBox="0 0 44 44" fill="none" stroke="var(--gold)" stroke-width="2" stroke-linecap="round"><circle cx="22" cy="15" r="5"/><circle cx="10" cy="20" r="4"/><circle cx="34" cy="20" r="4"/><path d="M13 34 a9 9 0 0 1 18 0 M3 33 a7 7 0 0 1 10 -6 M41 33 a7 7 0 0 0 -10 -6"/></svg></div><div class="benefit-name">Level of expertise</div><p class="benefit-text">Nemo enim ipsam vuptatem quia voluptas sit aspernatur aut</p></div>

<!-- appointment -->
<div class="skyline" role="img" aria-label="Faint line illustration of a city skyline"></div>
<h2 class="appt-title" style="top:2686px">BRAVO Estate Steward</h2>
<h2 class="appt-title" style="top:2736px">MAKE AN APPOINTMENT NOW</h2>
<p class="appt-text">Sed ut perspiciatis unde omnis iste natus error sit voluptatem accusantium doloremque laudantium, totam rem aperiam, eaque ipsa quae ab illo inventore veritatis et quasi architecto beatae vitae dicta sunt explicabo. Nemo enim ipsam voluptatem quia voluptas sit aspernatur aut odit aut fugit</p>
<div class="btn" style="left:484px;top:2912px;width:230px;height:39px;font-size:15px;color:var(--ink)">Request a Free Quote</div>

<!-- news -->
<section class="news"></section>
<h2 class="section-title" style="top:3143px">Latest News</h2>
<div class="rule" style="top:3208px;background:var(--ink)"></div>

<article class="card" style="left:143px;top:3257px;width:286px;height:377px">
  <div class="news-photo" role="img" aria-label="Photo of a contractor in a hard hat writing on a clipboard" style="background:linear-gradient(135deg,#9fb6c9,#5f7a95)"></div>
  <div class="date">DEC<br>2019</div>
  <h3 class="news-title center">Nemo enim ipsam voluptatem quia voluptas sit</h3>
  <p class="news-text center">Sed ut perspiciatis unde omnis iste natus error sit voluptatem accntium doloremque laudantium</p>
</article>
<article class="card" style="left:454px;top:3257px;width:286px;height:377px">
  <div class="news-photo" role="img" aria-label="Photo of a small wooden house model on paperwork with hands and a pen" style="background:linear-gradient(135deg,#c9d3dd,#8aa0b6)"></div>
  <div class="date">DEC<br>2019</div>
  <h3 class="news-title center">Nemo enim ipsam voluptatem quia voluptas sit</h3>
  <p class="news-text center">Sed ut perspiciatis unde omnis iste natus error sit voluptatem accntium doloremque laudantium</p>
</article>
<article class="card" style="left:765px;top:3257px;width:286px;height:377px">
  <div class="news-photo" role="img" aria-label="Photo of two builders in hard hats talking on a site" style="background:linear-gradient(135deg,#b9c4cc,#6c7a84)"></div>
  <div class="date">DEC<br>2019</div>
  <h3 class="news-title center">Nemo enim ipsam voluptatem quia voluptas sit</h3>
  <p class="news-text center">Sed ut perspiciatis unde omnis iste natus error sit voluptatem accntium doloremque laudantium</p>
</article>

<!-- testimonials -->
<h2 class="section-title" style="top:3788px">Client Testimonials</h2>
<div class="rule" style="top:3853px"></div>

<svg class="abs" style="left:118px;top:4014px" width="26" height="24" viewBox="0 0 26 24"><path d="M24 12 H3 M12 3 L3 12 L12 21" stroke="#555" stroke-width="3" fill="none"/></svg>
<svg class="abs" style="left:1053px;top:4014px" width="26" height="24" viewBox="0 0 26 24"><path d="M2 12 H23 M14 3 L23 12 L14 21" stroke="#555" stroke-width="3" fill="none"/></svg>

<div class="card" style="left:180px;top:3906px;width:405px;height:247px;text-align:left">
  <p class="quote-text">Sed ut perspiciatis unde omnis iste natus error sit voluptatem accusantium doloremque laudantium, totam rem aperiam, eaque ipsa quae ab illo inventore veritatis et quasi architecto beatae vitae dicta sunt explicabo.</p>
  <div class="avatar" role="img" aria-label="Portrait photo of the client"></div>
  <div class="quote-mark">”</div>
  <div class="who"><b>Dana Whitfield</b><br>BRAVO Estate Steward</div>
</div>
<div class="card" style="left:619px;top:3906px;width:407px;height:247px;text-align:left">
  <p class="quote-text">Sed ut perspiciatis unde omnis iste natus error sit voluptatem accusantium doloremque laudantium, totam rem aperiam, eaque ipsa quae ab illo inventore veritatis et quasi architecto beatae vitae dicta sunt explicabo.</p>
  <div class="avatar" role="img" aria-label="Portrait photo of the client"></div>
  <div class="quote-mark">”</div>
  <div class="who"><b>Dana Whitfield</b><br>BRAVO Estate Steward</div>
</div>

<!-- contact -->
<section class="footer"></section>
<svg class="abs" style="left:0;top:4230px" width="1200" height="90" viewBox="0 0 1200 90">
  <path d="M0 90 L0 45 Q600 -20 1200 45 L1200 90 Z" fill="var(--gold)"/>
  <path d="M0 90 L0 58 Q600 0 1200 58 L1200 90 Z" fill="var(--dark)"/>
</svg>
<h2 class="section-title" style="top:4334px;color:#fff">CONTACT US</h2>
<div class="rule" style="top:4398px"></div>

<div class="field" style="left:152px;top:4463px;width:255px;height:37px">Your Name</div>
<div class="field" style="left:152px;top:4532px;width:255px;height:37px">Your Phone</div>
<div class="field" style="left:152px;top:4601px;width:255px;height:38px">Your Email</div>
<div class="field area" style="left:429px;top:4463px;width:270px;height:106px">Your Message</div>
<div class="btn" style="left:429px;top:4599px;width:270px;height:40px;font-size:15px;color:var(--ink);font-weight:400;box-shadow:none">Send Messages</div>

<div class="info-icon" style="top:4464px"><svg width="18" height="22" viewBox="0 0 18 22"><path d="M9 1a7 7 0 0 0-7 7c0 5 7 13 7 13s7-8 7-13a7 7 0 0 0-7-7z" fill="var(--gold)"/><circle cx="9" cy="8" r="2.5" fill="var(--dark)"/></svg></div>
<p class="info-text" style="top:4457px">BRAVO Estate Steward<br>42 Harbor Lane, Maple Bay 10234,<br>United States</p>
<div class="info-icon" style="top:4537px"><svg width="20" height="20" viewBox="0 0 24 24"><path fill="var(--gold)" d="M6.6 10.8a15 15 0 0 0 6.6 6.6l2.2-2.2c.3-.3.7-.4 1-.2 1.1.4 2.3.6 3.6.6.6 0 1 .4 1 1V20c0 .6-.4 1-1 1A17 17 0 0 1 3 4c0-.6.4-1 1-1h3.5c.6 0 1 .4 1 1 0 1.3.2 2.5.6 3.6.1.3 0 .7-.2 1z"/></svg></div>
<p class="info-text" style="top:4538px">Phone :<br>555-0199-2040</p>
<div class="info-icon" style="top:4606px"><svg width="20" height="16" viewBox="0 0 20 16"><rect x="1" y="1" width="18" height="14" rx="1.5" fill="var(--gold)"/><path d="M1.5 2 L10 9 L18.5 2" stroke="var(--dark)" stroke-width="1.6" fill="none"/></svg></div>
<p class="info-text" style="top:4607px">Email :<br>hello@bravoestatesteward.example</p>

<div class="abs" style="left:0;top:4734px;width:1200px;height:1px;background:#474747"></div>
<p class="copyright">Copyright © BRAVO Estate Steward 2019. All rights reserved. | Privacy Policy</p>
<div class="social" style="left:911px"></div>
<div class="social" style="left:948px"></div>
<div class="social" style="left:985px"></div>
<div class="social" style="left:1022px"></div>

</body>
</html>
```